Franchise Beratung sucht Flyer Design
Mara hat das Faltblatt sehr professionell gestaltet! Was mir besonders gefällt ist die Tatsache, dass sie sich in das ausgefallene Thema Franchise sehr gut eingedacht hat, was bei der Auswahl der Bilder gut zu sehen ist. Außerdem hat sie den Text noch ergänzt und verbessert.
Zielgruppe
CapstoneGrowers ist eine Unternehmensberatung, die sich auf den Aufbau von neuen Franchisesystemen spezialisiert hat. Dabei setzen wir von Anfang an auf die Digitalisierung des Systems, um es leistungsstark und schnell zu gestalten.
Zielgruppe:
Der Flyer richtet sich vor allem an Unternehmer, die über die Expansion durch Franchising nachdenken. Er soll zur Kontaktaufnahme anregen und die klassischen Vorbehalte (zu teuer, brauche ich nicht, kann ich mir nicht leisten) nehmen.
Aufgabenstellung
Bei Form und Gestalt sind wir offen - er sollte aber sinnvoll auch per Post versendet werden können. Das Design sollte sich an unsere Website anpassen. Klar, modern und eher puristisch. Es darf aber ruhig etwas mehr Farbe verwendet werden.
Zusätzlich zu der Print-Vorlage möchten wir auch eine Version, die wir sinnvoll per Mail verschicken können.
Der Gewinner-Flyer sollte beschreibbar sein, so dass wir zukünftig einzelne Textpassagen ändern können.
Falls es Verbesserungsvorschläge zum Text gibt, sind auch diese herzlich willkommen!
Farben:
CMYK: 49 / 38 / 43 / 3 ( dunkelgrau )
CMYK: 24 / 17 / 21 / 0 ( hellgrau )
CMYK: 54 / 200 / 100/ 2 ( grün )
Schrifttyp: Für das Logo wurde eine eigene Schrift genutzt, da fehlen aber leider manche Buchstaben, deshalb möchten wir lieber eine andere Schrift, die gut zum Logo passt.

```html
<!DOCTYPE html>
<html lang="de">
<head>
<meta charset="utf-8">
<title>CapstoneGrowers – Faltblatt</title>
<link rel="stylesheet" href="https://fonts.googleapis.com/css2?family=Roboto:wght@300;400&display=swap">
<style>
:root{
  --green:#8cac22;
  --text:#4b4b4b;
  --muted:#8a8a8a;
  --strip:#9c9e97;
  --stage:#e2e2e2;
  --paper:#ffffff;
}
*{margin:0;padding:0;box-sizing:border-box}
html,body{width:1200px;height:1028px;overflow:hidden}
body{background:var(--stage);font-family:"Roboto",Arial,sans-serif;font-weight:300;color:var(--text);position:relative}
.sheet{position:absolute;background:var(--paper)}
.abs{position:absolute}
.photo{position:absolute}
.framed{border:3px solid #fff;box-shadow:0 0 0 1px #ddd}
.brand{color:var(--green);font-weight:300;display:flex;align-items:center;white-space:nowrap}
.brand .dot{border-radius:50%;background:var(--green);flex:none}
.green-bar{position:absolute;background:var(--green)}
.grey-strip{position:absolute;background:var(--strip)}
.panel-title{font-size:14px;line-height:16.5px;font-weight:300;color:#555}
.body-copy{font-size:6.6px;line-height:9.9px;color:#5a5a5a}
.body-copy p{margin-bottom:9.9px}
.accent{color:var(--green);font-weight:400;font-size:6.6px;line-height:9.9px}
.caption{font-size:5.6px;line-height:8.8px;color:var(--muted)}
.offer{position:absolute;left:752px;width:190px;display:flex;align-items:flex-start}
.offer .icon{width:31px;height:31px;flex:none;margin-top:-3px}
.offer .txt{margin-left:6px;font-size:6.6px;line-height:9.9px;color:#5a5a5a}
.offer .txt b{display:block;color:var(--green);font-weight:400}
</style>
</head>
<body>

<!-- Front cover -->
<section class="sheet cover" style="left:42px;top:42px;width:437px;height:943px">
  <div class="green-bar" style="left:0;top:0;width:437px;height:20px"></div>
  <div class="brand abs" style="left:30px;top:48px;font-size:38px;letter-spacing:-1px">
    <span class="dot" style="width:22px;height:22px;margin-right:10px"></span>CapstoneGrowers
  </div>
  <h1 class="abs" style="left:28px;top:210px;font-size:43px;line-height:47px;font-weight:300;color:#4a4a4a">Wir lassen Ihre Werte<br>wachsen!</h1>
  <div class="photo" role="img" aria-label="Foto: lächelnder Unternehmer mit Klemmbrett an einem Paket in einer Lagerhalle"
       style="left:0;top:335px;width:437px;height:588px;background:linear-gradient(160deg,#6b5a47 0%,#9b8a74 30%,#c7c3c4 55%,#8e7b63 78%,#4e4439 100%)"></div>
</section>

<!-- Outside spread -->
<section class="sheet outside" style="left:520px;top:42px;width:639px;height:451px">
  <div class="photo" role="img" aria-label="Hintergrundfoto: helles Bürogebäude mit Glasfassade"
       style="left:0;top:10px;width:424px;height:149px;background:linear-gradient(90deg,#d9dde0,#eef0f1 40%,#c9cdd0 70%,#e9ebec)"></div>
  <div class="photo framed" role="img" aria-label="Foto: Geschäftsleute im Gespräch in einer Lobby"
       style="left:10px;top:19px;width:189px;height:130px;background:linear-gradient(135deg,#eef1f2,#c8ccd0 50%,#9aa38b 80%,#e2e5e6)"></div>
  <div class="photo" role="img" aria-label="Foto: Geschäftsführerin am Telefon"
       style="left:230px;top:10px;width:194px;height:149px;background:linear-gradient(90deg,#e4e6e7,#c9a47e 45%,#2c2c2e 60%,#d6d9db)"></div>

  <div class="panel-title abs" style="left:20px;top:178px;width:180px">CapstoneGrowers –<br>Ihre Franchise-Beratung</div>
  <div class="body-copy abs" style="left:20px;top:220px;width:172px">
    <p>Der Wettbewerb der Zukunft wird nicht durch Produkte oder Leistungen entschieden. Sondern vor allem durch Menschen. Und Organisationen. Das gilt insbesondere für erfolgreiche Unternehmen, die in ihren Märkten gezielt expandieren wollen. Gerade in diesen Fällen ist Franchising oft eine besonders attraktive Form systematischer Multiplikation der eigenen Marke.</p>
    <p>Dabei im richtigen Moment das Richtige zu tun, unterscheidet die Besten von den Guten. Und genau auf diesem Weg wollen wir Sie begleiten. Mit all unserer Erfahrung im Aufbau sowie der fokussierten Weiterentwicklung bereits im Markt erfolgreich etablierter Franchise-Systeme.</p>
    <p class="accent">Mit all unserer Begeisterung für Marken mit Potenzial.</p>
  </div>

  <div class="caption abs" style="left:228px;top:180px">Helene Vorbrink,<br>Geschäftsführerin</div>
  <div class="panel-title abs" style="left:228px;top:291px">Neugierig geworden?</div>
  <div class="body-copy abs" style="left:228px;top:316px;width:190px">
    <p>Dann sollten wir uns kennenlernen.<br>Wir freuen uns auf Ihren Anruf!</p>
    <p>Helene Vorbrink Unternehmensberatung<br>Ahornweg 14<br>47799 Lindenfeld<br>Tel. +49 (0)2151 4408120<br>info@CapstoneGrowers.de</p>
    <p class="accent">Mehr Informationen finden Sie unter<br>www.CapstoneGrowers.de</p>
  </div>
  <div class="grey-strip" style="left:208px;top:441px;width:216px;height:10px"></div>

  <div class="green-bar" style="left:424px;top:0;width:215px;height:10px"></div>
  <div class="brand abs" style="left:442px;top:24px;font-size:17px">
    <span class="dot" style="width:10px;height:10px;margin-right:5px"></span>CapstoneGrowers
  </div>
  <div class="abs" style="left:444px;top:101px;font-size:20px;line-height:24px;color:#4a4a4a">Wir lassen Ihre Werte<br>wachsen!</div>
  <div class="photo" role="img" aria-label="Foto: Unternehmer mit Klemmbrett in einer Lagerhalle"
       style="left:424px;top:159px;width:215px;height:282px;background:linear-gradient(160deg,#7a6650,#a5957f 35%,#c5cad8 55%,#8c7a60 80%,#4f463a)"></div>
</section>

<!-- Inside spread -->
<section class="sheet inside" style="left:520px;top:534px;width:639px;height:451px">
  <div class="photo" role="img" aria-label="Hintergrundfoto: Laden und Büroumgebung"
       style="left:0;top:10px;width:430px;height:151px;background:linear-gradient(90deg,#6f6a63,#9a948a 40%,#d9dadb 70%,#eceeef)"></div>
  <div class="photo framed" role="img" aria-label="Foto: zwei Mitarbeiter hinter einer Ladentheke mit Tablet"
       style="left:10px;top:21px;width:195px;height:129px;background:linear-gradient(135deg,#4a4744,#8d7f73 45%,#c23b30 70%,#d8d2c8)"></div>
  <div class="photo framed" role="img" aria-label="Foto: Laptop mit Website und Videokonferenz"
       style="left:224px;top:21px;width:195px;height:129px;background:linear-gradient(135deg,#e8eaec,#cfd3d6 40%,#2b2d30 70%,#5f86b8)"></div>
  <div class="photo" role="img" aria-label="Foto: Beraterin im Gespräch mit einem Kunden"
       style="left:430px;top:10px;width:209px;height:151px;background:linear-gradient(90deg,#e9d7c2,#f2e9df 45%,#c9cbcf 75%,#f7f7f7)"></div>

  <div class="panel-title abs" style="left:20px;top:178px;width:180px">Wie funktioniert modernes<br>Franchising?</div>
  <div class="body-copy abs" style="left:20px;top:222px;width:176px">
    <p>Franchising ist der moderne und sympathische Weg, das eigene Unternehmen wachsen zu lassen. Das Know-how und die Marke, die Sie als Unternehmer über viele Jahre mühsam aufgebaut haben, geben Sie als Franchisegeber systematisch weiter. Und zwar an Menschen, die sich für Ihre Idee begeistern und sie mit lokalem Unternehmertum an neuen Orten zum Leben erwecken – die Franchisenehmer.</p>
    <p>Je besser Sie sich und Ihr Team dabei organisieren, desto leistungsfähiger können Sie agieren. CapstoneGrowers setzt deshalb von Anfang an auf digitale Bausteine. Dadurch bleiben die Anfangsinvestitionen für Sie überschaubar und Sie können die Franchisenehmer optimal unterstützen.</p>
    <p class="accent">Davon profitiert das gesamte System!</p>
  </div>

  <div class="panel-title abs" style="left:235px;top:178px">Beratung nach Maß</div>
  <div class="body-copy abs" style="left:235px;top:204px;width:180px">
    <p>Wir unterstützen zukünftige Lizenz- und Franchisegeber individuell nach ihren Bedürfnissen, ihrem Budget und in ihrem Tempo.</p>
  </div>

  <div class="grey-strip" style="left:0;top:441px;width:215px;height:10px"></div>
  <div class="grey-strip" style="left:430px;top:441px;width:209px;height:10px"></div>

  <div class="panel-title abs" style="left:450px;top:178px;width:180px">Wachsen Sie erfolgreich –<br>auf lange Sicht</div>
  <div class="body-copy abs" style="left:450px;top:222px;width:176px">
    <p>Wer kurzfristig denkt, denkt langfristig falsch. Das gilt besonders beim Aufbau eines Franchisesystems.</p>
    <p>Unternehmer, die erfolgreich ins Franchising starten wollen, setzen deshalb auf CapstoneGrowers. Durch unsere langjährige Expertise wissen wir, was wann zu tun ist. Dabei setzen wir auf digitale Medien und Tools, um das System leistungsstark und zukunftssicher zu gestalten.</p>
    <p class="accent">Damit Ihre Werte wachsen!</p>
  </div>
  <div class="brand abs" style="left:508px;top:408px;font-size:12.5px">
    <span class="dot" style="width:7px;height:7px;margin-right:4px"></span>CapstoneGrowers
  </div>
</section>

<!-- Offer list -->
<div class="offer" style="top:782px">
  <svg class="icon" viewBox="0 0 32 32"><circle cx="16" cy="16" r="15.5" fill="#dcdcdc"/><circle cx="16" cy="16" r="10" fill="#8e8e8e"/><circle cx="16" cy="16" r="5.5" fill="none" stroke="#fff" stroke-width="1"/><path d="M16 13v3h2.5" fill="none" stroke="#fff" stroke-width="1"/></svg>
  <div class="txt"><b>Die Ungeduldigen: der Franchise Quick-Check</b>Sie erfahren an einem Tag, ob Ihre Idee Franchise-tauglich ist und die nächsten Schritte.</div>
</div>
<div class="offer" style="top:821px">
  <svg class="icon" viewBox="0 0 32 32"><circle cx="16" cy="16" r="15.5" fill="#dcdcdc"/><circle cx="16" cy="16" r="10" fill="#8e8e8e"/><circle cx="16" cy="16" r="5" fill="none" stroke="#fff" stroke-width="2" stroke-dasharray="2 1.2"/><circle cx="16" cy="16" r="2" fill="#fff"/></svg>
  <div class="txt"><b>Die Entwickler: Franchise-Coaching</b>Sie entwickeln Ihr Konzept und wir steuern unser Fachwissen sowie unser Netzwerk bei.</div>
</div>
<div class="offer" style="top:860px">
  <svg class="icon" viewBox="0 0 32 32"><circle cx="16" cy="16" r="15.5" fill="#dcdcdc"/><circle cx="16" cy="16" r="10" fill="#8e8e8e"/><rect x="11" y="12" width="10" height="7" fill="none" stroke="#fff" stroke-width="1"/><path d="M14 21h4" stroke="#fff" stroke-width="1"/></svg>
  <div class="txt"><b>Die Wissbegierigen: interaktive Webinare</b>Lernen Sie alles rund um den Franchise-Aufbau bequem vom Büro aus in kleinen Einheiten.</div>
</div>
<div class="offer" style="top:899px">
  <svg class="icon" viewBox="0 0 32 32"><circle cx="16" cy="16" r="15.5" fill="#dcdcdc"/><circle cx="16" cy="16" r="10" fill="#8e8e8e"/><rect x="12.5" y="11" width="7" height="10" fill="none" stroke="#fff" stroke-width="1"/><path d="M14 14h4M14 16h4M14 18h4" stroke="#fff" stroke-width=".7"/></svg>
  <div class="txt"><b>Die Macher: ausgefeilte Konzepte</b>Wir übernehmen für Sie die konzeptionelle Arbeit, natürlich in enger Abstimmung mit Ihnen.</div>
</div>
<div class="offer" style="top:938px">
  <svg class="icon" viewBox="0 0 32 32"><circle cx="16" cy="16" r="15.5" fill="#dcdcdc"/><circle cx="16" cy="16" r="10" fill="#8e8e8e"/><circle cx="16" cy="16" r="5" fill="none" stroke="#fff" stroke-width="1"/><text x="16" y="18.3" font-size="6" text-anchor="middle" fill="#fff" font-family="Roboto,Arial,sans-serif">€</text></svg>
  <div class="txt"><b>Die Sparsamen: per Videocall</b>Statt Zeit und Geld in die Anreise zu investieren, unterstützen wir Sie gerne per Videokonferenz.</div>
</div>

</body>
</html>
```